Engineering Consultant Business Card

I'm starting a new business as a high-end engineering consultant in a niche field. I've attached the jpg for my logo plus the branding guideline document that I've been following. You can see my business website here: www.tarvikworks.com
I'd like a business card that has the logo on one side, then the other side has (in any order): Tarvik Works, Inc.
Dana Whitlock
President and Chief EMC Engineer
www.tarvikworks.com
dana@tarvikworks.com
Optional: motto "We will solve your EMC problems as early as possible—ideally before they even start."
I'm not planning on including a phone number
Target Market(s)
Businesses, especially makers of electronics hardware
Industry/Entity Type
Electrical engineering
Contact Information for Business Card
Company name, my name, website, email

```html
<!DOCTYPE html>
<html lang="en">
<head>
<meta charset="utf-8">
<title>Tarvik Works, Inc. – Business Card</title>
<link rel="stylesheet" href="https://fonts.googleapis.com/css2?family=Montserrat:wght@400;500;600;700&display=swap">
<style>
  :root {
    --stage: #3c4141;
    --card-black: #000000;
    --card-white: #ffffff;
    --navy: #2e3f9a;
    --sky: #4aaed0;
    --ink-light: #ffffff;
  }
  * { box-sizing: border-box; margin: 0; padding: 0; }
  html, body {
    width: 1200px; height: 1200px; overflow: hidden;
    background: var(--stage);
    font-family: "Montserrat", Arial, sans-serif;
  }
  .stage { position: relative; width: 1200px; height: 1200px; }
  .card {
    position: absolute; left: 150px;
    width: 900px; height: 514px;
    border-radius: 24px; overflow: hidden;
  }
  .card-front { top: 50px; background: var(--card-black); }
  .card-back { top: 620px; background: var(--card-white); }
  .card-waves { position: absolute; inset: 0; width: 100%; height: 100%; }

  .front-mark {
    position: absolute; left: 0; right: 0; top: 120px;
    display: flex; align-items: center; justify-content: center; gap: 18px;
  }
  .front-mark .mark-dot {
    width: 46px; height: 46px; border-radius: 50%;
    border: 5px solid var(--ink-light);
  }
  .front-mark .mark-name {
    color: var(--ink-light); font-weight: 600; font-size: 48px; letter-spacing: 1px;
  }

  .back-brand {
    position: absolute; left: 110px; top: 36px;
    display: flex; flex-direction: column; align-items: flex-start;
    color: var(--navy);
  }
  .back-brand .brand-row { display: flex; align-items: center; gap: 10px; }
  .back-brand .mark-dot {
    width: 26px; height: 26px; border-radius: 50%; border: 4px solid var(--navy);
  }
  .back-brand .mark-name { font-weight: 600; font-size: 26px; color: var(--navy); }
  .back-brand .company { font-size: 16px; font-weight: 400; margin-top: 6px; }

  .person { position: absolute; left: 110px; top: 168px; color: var(--navy); }
  .person .name { font-weight: 700; font-size: 42px; letter-spacing: 1px; line-height: 1.1; }
  .person .title { font-weight: 400; font-size: 21px; margin-top: 4px; }

  .contact {
    position: absolute; display: flex; align-items: center; gap: 16px;
    color: var(--navy); font-size: 21px; font-weight: 400;
  }
  .contact svg { width: 24px; height: 24px; flex: none; }
  .contact-email { left: 520px; top: 110px; }
  .contact-web { left: 60px; top: 350px; }
</style>
</head>
<body>
<main class="stage">

  <section class="card card-front" aria-label="Card front">
    <svg class="card-waves" viewBox="0 0 900 514" preserveAspectRatio="none" aria-hidden="true">
      <path d="M0,396 C320,392 600,280 900,150" fill="none" stroke="var(--sky)" stroke-width="9"/>
      <path d="M0,514 L0,442 C330,438 610,320 900,200 L900,514 Z" fill="var(--navy)"/>
    </svg>
    <div class="front-mark">
      <span class="mark-dot"></span>
      <span class="mark-name">Tarvik Works</span>
    </div>
  </section>

  <section class="card card-back" aria-label="Card back">
    <svg class="card-waves" viewBox="0 0 900 514" preserveAspectRatio="none" aria-hidden="true">
      <path d="M0,418 C350,420 640,330 900,200" fill="none" stroke="var(--sky)" stroke-width="9"/>
      <path d="M0,514 L0,466 C360,466 660,370 900,236 L900,514 Z" fill="var(--navy)"/>
    </svg>

    <div class="back-brand">
      <div class="brand-row">
        <span class="mark-dot"></span>
        <span class="mark-name">Tarvik Works</span>
      </div>
      <span class="company">Tarvik Works, Inc.</span>
    </div>

    <div class="person">
      <h1 class="name">DANA WHITLOCK</h1>
      <p class="title">President and Chief EMC Engineer</p>
    </div>

    <p class="contact contact-email">
      <svg viewBox="0 0 24 24" aria-hidden="true"><rect x="2" y="5" width="20" height="14" fill="none" stroke="var(--navy)" stroke-width="1.6"/><path d="M2,5 L12,13 L22,5" fill="none" stroke="var(--navy)" stroke-width="1.6"/></svg>
      <span>dana@tarvikworks.com</span>
    </p>

    <p class="contact contact-web">
      <svg viewBox="0 0 24 24" aria-hidden="true"><circle cx="12" cy="12" r="10" fill="none" stroke="var(--navy)" stroke-width="1.6"/><ellipse cx="12" cy="12" rx="4.5" ry="10" fill="none" stroke="var(--navy)" stroke-width="1.4"/><path d="M2,12 H22 M4,7 H20 M4,17 H20" stroke="var(--navy)" stroke-width="1.4"/></svg>
      <span>www.tarvikworks.com</span>
    </p>
  </section>

</main>
</body>
</html>
```